Progressive Architecture and Urban Planning Studio - Stationery Design

The Kestrel Collective: a small boutique Architectural and Urban Planning Studio based in Natal/ RN, Brazil, about to open branches in South Africa and West Africa, established to provide high quality, innovative design and personal client service for projects worldwide. Our approach to Architecture: Minimal - Less is More, so to speak, but with an edge! Strive to produce "clean" projects - stripped of all that can be stripped, no excesses. Got our Logo right here with Pixel Harbor, and hope to do the same with our stationery (were informed that includes business cards, letterhead and envelopes). Since we'll be using two clour schemes, we want at least one using a black background (business card). We'll also allow manipulation of our logo if it helps the final design. Good Luck!

Font styles to use
Other font styles liked:
• Nexa

Colors

Designer to choose colors to be used in the design.

Requirements
Must have
• Business Cards/ Letterheads with the following address:
Rua Olavo Pereira 2741, Vale Dourado, Natal/RN
Should be able to edit it.

```html
<!DOCTYPE html>
<html lang="en">
<head>
<meta charset="utf-8">
<title>The Kestrel Collective — Stationery</title>
<link rel="stylesheet" href="https://fonts.googleapis.com/css2?family=Montserrat:wght@300&family=Lato:wght@400;700&display=swap">
<style>
  :root {
    --backdrop: #eceeee;
    --paper: #ffffff;
    --paper-shade: #e4e4e4;
    --ink: #1e1e1e;
    --charcoal: #262626;
    --charcoal-light: #474747;
    --brand-red: #d0343c;
    --brand-grey: #6a6a6a;
  }
  * { box-sizing: border-box; margin: 0; padding: 0; }
  html, body { width: 1200px; height: 796px; overflow: hidden; }
  body {
    position: relative;
    background: var(--backdrop);
    font-family: "Lato", Arial, sans-serif;
    color: var(--ink);
  }
  .piece { position: absolute; overflow: hidden; }
  .texture { position: absolute; }

  .brand { position: absolute; display: flex; align-items: center; gap: 6px; white-space: nowrap; }
  .brand-mark { background: var(--brand-red); flex: none; }
  .brand-name {
    font-family: "Montserrat", Arial, sans-serif;
    font-weight: 300;
    text-transform: uppercase;
    color: var(--brand-grey);
  }
  .red-bar { position: absolute; background: var(--brand-red); }

  /* Letterhead */
  .letterhead { left: 289px; top: 99px; width: 298px; height: 417px; background: var(--paper); box-shadow: 0 0 0 1px #dcdcdc; }
  .letterhead .texture { left: 0; top: 300px; width: 200px; height: 117px; background: linear-gradient(160deg, #ffffff 0%, #f1f1f1 100%); }
  .letterhead .brand { left: 16px; top: 24px; }
  .letterhead .brand-mark { width: 12px; height: 12px; }
  .letterhead .brand-name { font-size: 7.2px; letter-spacing: 1.5px; }
  .letter-body { position: absolute; left: 27px; top: 86px; width: 240px; font-size: 5.1px; line-height: 6.3px; }
  .letter-body p { margin-bottom: 6.3px; }
  .letter-body .gap { margin-bottom: 19px; }
  .letterhead-footer { position: absolute; left: 60px; top: 389px; font-size: 5.2px; font-weight: 700; white-space: nowrap; }

  /* Folder */
  .folder { left: 633px; top: 81px; width: 347px; height: 440px; }
  .folder .texture { left: 0; top: 0; width: 347px; height: 440px; background: linear-gradient(135deg, var(--charcoal) 0%, var(--charcoal-light) 100%); }
  .folder .brand { left: 55px; top: 278px; gap: 10px; }
  .folder .brand-mark { width: 30px; height: 30px; }
  .folder .brand-name { font-size: 13px; letter-spacing: 2.6px; color: #e6e6e6; }

  /* Business cards */
  .card { left: 185px; width: 133px; height: 77px; }
  .card .texture { left: 0; top: 0; width: 133px; height: 77px; background: linear-gradient(135deg, #222222 0%, #333333 100%); }
  .card-front { top: 551px; }
  .card-front .brand { left: 12px; top: 34px; gap: 4px; }
  .card-front .brand-mark { width: 7px; height: 7px; }
  .card-front .brand-name { font-size: 4.6px; letter-spacing: 1px; color: #d8d8d8; }
  .card-back { top: 645px; }
  .card-back .brand { left: 10px; top: 10px; gap: 4px; }
  .card-back .brand-mark { width: 6px; height: 6px; }
  .card-back .brand-name { font-size: 4.2px; letter-spacing: 0.9px; color: #d8d8d8; }
  .card-person { position: absolute; left: 12px; top: 33px; color: #fff; }
  .card-person .name { font-size: 6px; font-weight: 700; line-height: 7px; }
  .card-person .role { font-size: 4px; line-height: 5px; }
  .card-contact { position: absolute; top: 48px; font-size: 3.5px; line-height: 4.6px; color: #e8e8e8; white-space: nowrap; }
  .card-contact.left { left: 12px; }
  .card-contact.right { left: 82px; }

  /* Envelopes */
  .envelope-plain { left: 352px; top: 565px; width: 333px; height: 157px; background: linear-gradient(180deg, #f6f6f6 0%, var(--paper-shade) 100%); }
  .envelope-plain .brand { left: 18px; top: 17px; }
  .envelope-plain .brand-mark { width: 12px; height: 12px; }
  .envelope-plain .brand-name { font-size: 7.2px; letter-spacing: 1.6px; }
  .envelope-flap { left: 711px; top: 563px; width: 330px; height: 159px; background: var(--paper); box-shadow: 0 0 0 1px #dedede; }
  .envelope-flap .flap { position: absolute; left: 0; top: 0; }
  .envelope-flap .brand { left: 0; width: 330px; top: 20px; justify-content: center; gap: 4px; }
  .envelope-flap .brand-mark { width: 8px; height: 8px; }
  .envelope-flap .brand-name { font-size: 5px; letter-spacing: 1.1px; color: #e0e0e0; }
</style>
</head>
<body>

<section class="piece letterhead" aria-label="Letterhead">
  <div class="texture" role="img" aria-label="Soft area for the scattered thin grey line decoration"></div>
  <div class="brand">
    <span class="brand-mark"></span>
    <span class="brand-name">The Kestrel Collective</span>
  </div>
  <div class="red-bar" style="left:169px; top:26px; width:129px; height:7px;"></div>
  <div class="letter-body">
    <p><strong>52 Alder Court,<br>Fairhaven, MA 02719.</strong></p>
    <p><strong>January 29th, 2011</strong></p>
    <p>Mr. Halvorsen<br>President, Halvorsen Learning Center<br>18 Birchwood Row<br>Portland, ME 04101</p>
    <p>Dear Mr. Halvorsen:</p>
    <p class="gap">In the first paragraph, one needs to give a brief introduction of oneself. One should also give reference to the purpose of the letter in brief.<br>The second paragraph needs to give the details of the letter and its need. This paragraph is mostly longer than the others and plays the main role in the letter. Keep the sentences short and to the point. Avoid using complex words and sentences.</p>
    <p>The third and last paragraph is the conclusion of the letter and can be kept short.</p>
    <p>Sincerely,</p>
    <p>(this is where the signature of the writer will be placed)</p>
    <p>Dana Moreau<br>Read more at Lettercraft: http://www.lettercraft-notes.com/articles/formal-letter-layout.html</p>
  </div>
  <p class="letterhead-footer">Rua Olavo Pereira 2741, Vale Dourado, Natal/RN | 084.555.0142</p>
  <div class="red-bar" style="left:60px; top:398px; width:238px; height:6px;"></div>
</section>

<section class="piece folder" aria-label="Presentation folder">
  <div class="texture" role="img" aria-label="Charcoal background with scattered thin grey line decoration"></div>
  <div class="brand">
    <span class="brand-mark"></span>
    <span class="brand-name">The Kestrel Collective</span>
  </div>
  <div class="red-bar" style="left:111px; top:412px; width:236px; height:6px;"></div>
</section>

<section class="piece card card-front" aria-label="Business card front">
  <div class="texture" role="img" aria-label="Charcoal background with scattered thin grey line decoration"></div>
  <div class="brand">
    <span class="brand-mark"></span>
    <span class="brand-name">The Kestrel Collective</span>
  </div>
</section>

<section class="piece card card-back" aria-label="Business card back">
  <div class="texture" role="img" aria-label="Charcoal background with scattered thin grey line decoration"></div>
  <div class="brand">
    <span class="brand-mark"></span>
    <span class="brand-name">The Kestrel Collective</span>
  </div>
  <div class="card-person">
    <p class="name">Your Name</p>
    <p class="role">Position</p>
  </div>
  <div class="card-contact left">
    <p>Address Rua Olavo 2741</p>
    <p>Natal/RN Brazil</p>
    <p>Phone 084 555 0142</p>
  </div>
  <div class="card-contact right">
    <p>Fax 084 555 0143</p>
    <p>Email hi@kestrel.co</p>
    <p>Web kestrel.co</p>
  </div>
</section>

<section class="piece envelope-plain" aria-label="Envelope front">
  <div class="brand">
    <span class="brand-mark"></span>
    <span class="brand-name">The Kestrel Collective</span>
  </div>
  <div class="red-bar" style="left:70px; top:146px; width:263px; height:5px;"></div>
</section>

<section class="piece envelope-flap" aria-label="Envelope back">
  <svg class="flap" width="330" height="52" viewBox="0 0 330 52" aria-hidden="true">
    <polygon points="0,0 330,0 312,50 18,50" fill="var(--charcoal-light)"/>
  </svg>
  <div class="brand">
    <span class="brand-mark"></span>
    <span class="brand-name">The Kestrel Collective</span>
  </div>
  <div class="red-bar" style="left:68px; top:146px; width:262px; height:5px;"></div>
</section>

</body>
</html>
```